Etiketten für Gin
Zielgruppe
Unser Firma ist Errichter für Sicherheitstechnik und hat letztes Jahr einen eigenen Gin entwickelt und Ihn unter dem Namen Nachtfalke an Kunden verschenkt und ein paar Märkte zur Probe damit ausgestattet.
Aufgabenstellung
Das derzeitige Design ist schon nicht schlecht aber wurde von uns selber entwickelt und soll nun professionell Designt und Marktfähig für WOLMA und Co gemacht werden. Es soll eine White und Black Edition geben, die beiden unterscheiden sich im Geschmack und haben entweder Silber oder Gold Flakes mit drin. Daher muss das eine Etikett im Backround Weiß und das ander Schwarz sein.
Wichtig !! Der Totenkopf muss für beide Flaschen bleiben, der bestehende Totenkopf ist nicht in Beton gemeißelt, daher macht uns coole kreative Vorschläge.

```html
<!DOCTYPE html>
<html lang="de">
<head>
<meta charset="utf-8">
<title>Nachtfalke Gin – Etiketten</title>
<link rel="stylesheet" href="https://fonts.googleapis.com/css2?family=Berkshire+Swash&family=Alfa+Slab+One&family=Old+Standard+TT:wght@700&display=swap">
<style>
  :root {
    --page: #ffffff;
    --black-ground: #0e0c10;
    --black-gin: #3a3a3c;
    --gold: #c9a86a;
    --purple: #6b3fae;
    --white-ground: #f4f4f6;
    --silver: #b4b4b9;
    --white-gin: #dcdce0;
    --ink: #1d1b20;
    --parchment: #e9dcc0;
  }
  * { margin: 0; padding: 0; box-sizing: border-box; }
  html, body { width: 806px; height: 1200px; overflow: hidden; background: var(--page); }
  .canvas {
    width: 806px; height: 1200px;
    display: flex; flex-direction: column; align-items: center; justify-content: center; gap: 90px;
  }
  .label { width: 600px; height: 450px; display: block; }
  .brand-name { font-family: "Alfa Slab One", serif; font-size: 44px; letter-spacing: 2px; fill: var(--purple); }
  .gin-word { font-family: "Alfa Slab One", serif; font-size: 290px; }
  .spec { font-family: "Alfa Slab One", serif; font-size: 19px; letter-spacing: 1px; }
  .edition { font-family: "Berkshire Swash", cursive; font-size: 32px; fill: #ffffff; }
  .scroll-text { font-family: "Old Standard TT", serif; font-size: 8.5px; fill: var(--ink); }
  .scroll { fill: var(--parchment); stroke: #8a7550; }

  .label--black .ground { fill: var(--black-ground); stroke: var(--gold); }
  .label--black .gin-word { fill: var(--black-gin); }
  .label--black .spec { fill: var(--gold); }
  .label--black .edition-band { fill: var(--purple); stroke: var(--gold); }

  .label--white .ground { fill: var(--white-ground); stroke: var(--silver); }
  .label--white .gin-word { fill: var(--white-gin); }
  .label--white .spec { fill: var(--ink); }
  .label--white .edition-band { fill: var(--purple); stroke: var(--silver); }
</style>
</head>
<body>
<main class="canvas">

  <svg class="label label--black" viewBox="0 0 720 540" aria-label="Etikett Nachtfalke Gin, Ausführung Schwarz">
    <defs>
      <linearGradient id="skull-black" x1="0" y1="0" x2="0" y2="1">
        <stop offset="0" stop-color="#7a55b8"/>
        <stop offset="0.35" stop-color="#d8c9a3"/>
        <stop offset="1" stop-color="#9a9aa2"/>
      </linearGradient>
    </defs>
    <path class="ground" stroke-width="5" d="M4,110 L180,110 C250,4 470,4 540,110 L716,110 L716,420 C560,560 160,560 4,420 Z"/>
    <text class="gin-word" x="360" y="400" text-anchor="middle">GIN</text>
    <text class="brand-name" x="360" y="104" text-anchor="middle">NACHTFALKE</text>
    <rect x="265" y="130" width="190" height="275" rx="24" fill="url(#skull-black)" role="img" aria-label="Illustration: Totenkopf als Becher mit Wacholderbeeren, gekreuzte Brecheisen und Ginflasche"/>
    <text class="spec" x="190" y="350" text-anchor="middle">40VOL.</text>
    <text class="spec" x="530" y="350" text-anchor="middle">500ML</text>
    <path class="scroll" stroke-width="1.5" d="M240,408 L480,408 L470,445 L250,445 Z"/>
    <text class="scroll-text" x="360" y="424" text-anchor="middle">Mit diesem hochwertigen Gin hast du eine sehr</text>
    <text class="scroll-text" x="360" y="436" text-anchor="middle">gute Beute gemacht. Viel Spaß beim genießen.</text>
    <path class="edition-band" stroke-width="3" d="M195,458 L525,440 L530,495 L200,512 Z"/>
    <text class="edition" x="362" y="488" text-anchor="middle" transform="rotate(-3 362 478)">Ausführung Schwarz</text>
  </svg>

  <svg class="label label--white" viewBox="0 0 720 540" aria-label="Etikett Nachtfalke Gin, Ausführung Weiß">
    <defs>
      <linearGradient id="skull-white" x1="0" y1="0" x2="0" y2="1">
        <stop offset="0" stop-color="#7a55b8"/>
        <stop offset="0.35" stop-color="#d8c9a3"/>
        <stop offset="1" stop-color="#b4b4bc"/>
      </linearGradient>
    </defs>
    <path class="ground" stroke-width="5" d="M4,110 L180,110 C250,4 470,4 540,110 L716,110 L716,420 C560,560 160,560 4,420 Z"/>
    <text class="gin-word" x="360" y="400" text-anchor="middle">GIN</text>
    <text class="brand-name" x="360" y="104" text-anchor="middle">NACHTFALKE</text>
    <rect x="265" y="130" width="190" height="275" rx="24" fill="url(#skull-white)" role="img" aria-label="Illustration: Totenkopf als Becher mit Wacholderbeeren, gekreuzte Brecheisen und Ginflasche"/>
    <text class="spec" x="190" y="350" text-anchor="middle">40VOL.</text>
    <text class="spec" x="530" y="350" text-anchor="middle">500ML</text>
    <path class="scroll" stroke-width="1.5" d="M240,408 L480,408 L470,445 L250,445 Z"/>
    <text class="scroll-text" x="360" y="424" text-anchor="middle">Mit diesem hochwertigen Gin hast du eine sehr</text>
    <text class="scroll-text" x="360" y="436" text-anchor="middle">gute Beute gemacht. Viel Spaß beim genießen.</text>
    <path class="edition-band" stroke-width="3" d="M195,458 L525,440 L530,495 L200,512 Z"/>
    <text class="edition" x="362" y="488" text-anchor="middle" transform="rotate(-3 362 478)">Ausführung Weiß</text>
  </svg>

</main>
</body>
</html>
```